Letterhead Design Project

Attached is our new Logo and a copy of our old letter head
Looking to rebrand with our new logo

Reason: I want to show a business card design

Industry/Entity Type

Film Production

Colors

Designer to choose colors to be used in the design.

Requirements
Must have
• The information on the old letterhead

```html
<!DOCTYPE html>
<html lang="en">
<head>
<meta charset="utf-8">
<title>Marrowby International Letterhead</title>
<link href="https://fonts.googleapis.com/css2?family=Josefin+Sans:wght@700&family=Open+Sans:wght@400&display=swap" rel="stylesheet">
<style>
  :root {
    --bg: #d9dadb;
    --paper: #ffffff;
    --sky: #a9d3e2;
    --sky-deep: #5fa9c9;
    --orange: #e8731f;
    --navy: #1d3a5a;
    --grey-text: #4f6274;
  }
  html, body {
    margin: 0;
    width: 1200px;
    height: 960px;
    overflow: hidden;
    background: var(--bg);
  }
  .letterhead {
    position: absolute;
    left: 282px;
    top: 30px;
    width: 636px;
    height: 900px;
    background: var(--paper);
    overflow: hidden;
    box-shadow: 0 6px 24px rgba(0,0,0,0.15);
  }
  .decor {
    position: absolute;
    inset: 0;
    width: 636px;
    height: 900px;
  }
  .brand {
    position: absolute;
    right: 28px;
    top: 44px;
    text-align: right;
    font-family: "Josefin Sans", sans-serif;
    font-weight: 700;
    color: var(--navy);
    line-height: 1;
  }
  .brand-name { font-size: 30px; letter-spacing: 1px; }
  .brand-sub { font-size: 11px; letter-spacing: 2.4px; margin-top: 6px; }
  .contact {
    position: absolute;
    right: 28px;
    top: 124px;
    text-align: right;
  }
  .tagline {
    font-family: "Josefin Sans", sans-serif;
    font-weight: 700;
    font-size: 13px;
    color: var(--orange);
    margin: 0 0 4px;
  }
  .contact-line {
    font-family: "Open Sans", sans-serif;
    font-size: 11.5px;
    color: var(--grey-text);
    margin: 0 0 2px;
  }
  .footer {
    position: absolute;
    left: 0;
    right: 0;
    top: 812px;
    text-align: center;
  }
  .divisions {
    font-family: "Josefin Sans", sans-serif;
    font-weight: 700;
    font-size: 11.5px;
    color: var(--navy);
    margin: 0 0 3px;
  }
  .legal {
    font-family: "Open Sans", sans-serif;
    font-size: 10px;
    color: var(--grey-text);
    margin: 0;
    line-height: 1.25;
  }
</style>
</head>
<body>
  <main class="letterhead">
    <svg class="decor" viewBox="0 0 636 900">
      <defs>
        <linearGradient id="header-tone" x1="0" y1="0" x2="1" y2="0">
          <stop offset="0" stop-color="var(--sky-deep)"/>
          <stop offset="1" stop-color="var(--sky)"/>
        </linearGradient>
      </defs>
      <path class="header-field" role="img" aria-label="Decorative header graphic in blue and orange tones"
            d="M0 0 H560 Q300 60 0 240 Z" fill="url(#header-tone)"/>
      <path class="footer-field" role="img" aria-label="Decorative footer graphic in blue and orange tones"
            d="M0 730 Q320 800 636 720 V900 H0 Z" fill="var(--sky)"/>
    </svg>

    <div class="brand">
      <div class="brand-name">MARROWBY</div>
      <div class="brand-sub">INTERNATIONAL</div>
    </div>

    <div class="contact">
      <p class="tagline">SUPPLY &amp; MANAGEMENT OF INFRASTRUCTURE &amp; LOGISTICS</p>
      <p class="contact-line">P.O. Box 482 Northgate QLD 4013&nbsp;&nbsp; P.O. Box 317 Penrith NSW 2750</p>
      <p class="contact-line">Phone no.: 0400 128 570 | Email add.: hello@marrowby.com.au</p>
    </div>

    <footer class="footer">
      <p class="divisions">MARROWBY FILM SERVICES | MARROWBY PILOT ESCORTS | MARROWBY TOUR MANAGEMENT | MARROWBY DRIVER</p>
      <p class="legal">are divisions of MARROWBY International Pty Ltd</p>
      <p class="legal">ACN 204 718 362&nbsp; ABN 41 204 718 362</p>
    </footer>
  </main>
</body>
</html>
```